New Business Card for Casual Beachfront Cafe

Quirky Beachfront Cafe at Moana, South Australia needs a DOUBLE SIDED business card to print on PrintHarbor.

Target Market(s)

Business Cards sit on the counter for Guests to take with them. Please view our website www.saltreefcafe.com.au to get a feel for the Cafe. You may also view our Instagram at @saltreefcafe

Industry/Entity Type

Cafe / Restaurant

Contact Information for Business Card

Information equivalent to: Breakfast, Lunch, Dinner, Coffee, Takeaway / 117 Parade Kelpwater QV 4820 / Menu & Opening Hours: www.saltreefcafe.com.au / ph (08) 8461 9273

Requirements
Must have
• Information equivalent to: Breakfast, Lunch, Dinner, Coffee, Takeaway / 117 Parade Kelpwater QV 4820 / Menu & Opening Hours: www.saltreefcafe.com.au / ph (08) 8461 9273
Nice to have
• Potentially some of our trademark colours (Cafe can be searched via Seekly)
Should not have
• Must NOT have image of the building. May have the logo provided on one side but not necessarily, depending on how you wish to design the card

```html
<!DOCTYPE html>
<html lang="en">
<head>
<meta charset="utf-8">
<title>Salt Reef Cafe – Business Card</title>
<link href="https://fonts.googleapis.com/css2?family=Montserrat:wght@400;700;800&display=swap" rel="stylesheet">
<style>
  :root {
    --backdrop: #e9e6e1;
    --card-teal: #3a5f63;
    --accent-yellow: #f6f000;
    --card-shadow: rgba(0, 0, 0, 0.22);
  }
  * { box-sizing: border-box; margin: 0; padding: 0; }
  html, body {
    width: 1200px;
    height: 815px;
    overflow: hidden;
    background: var(--backdrop);
    font-family: "Montserrat", sans-serif;
  }
  .sheet {
    width: 1200px;
    height: 815px;
    display: flex;
    flex-direction: column;
    align-items: center;
    justify-content: center;
    gap: 30px;
  }
  .card {
    position: relative;
    width: 600px;
    height: 367px;
    background: var(--card-teal);
    border: 2px solid var(--accent-yellow);
    box-shadow: 0 6px 18px var(--card-shadow);
    color: var(--accent-yellow);
  }
  .brand-name {
    font-weight: 800;
    text-transform: uppercase;
    text-align: center;
    line-height: 1;
    letter-spacing: 1px;
    color: var(--accent-yellow);
  }
  .brand-name span { display: block; }

  /* back side */
  .card--back {
    display: flex;
    align-items: center;
    justify-content: center;
  }
  .card--back .brand-name { font-size: 62px; }
  .card--back .brand-name span + span { margin-top: 6px; }

  /* front side */
  .card--front .brand-name {
    position: absolute;
    top: 40px;
    left: 0;
    right: 0;
    font-size: 44px;
  }
  .card--front .brand-name span + span { margin-top: 4px; }
  .services {
    position: absolute;
    top: 182px;
    left: 0;
    right: 0;
    text-align: center;
    font-weight: 700;
    font-size: 22px;
  }
  .menu-label {
    position: absolute;
    top: 216px;
    left: 0;
    right: 0;
    text-align: center;
    font-weight: 700;
    font-size: 18px;
  }
  .contact-list {
    position: absolute;
    left: 30px;
    bottom: 40px;
    list-style: none;
    font-weight: 400;
    font-size: 15px;
  }
  .contact-list li {
    display: flex;
    align-items: center;
    gap: 10px;
    margin-top: 8px;
    line-height: 18px;
  }
  .contact-list svg { width: 15px; height: 15px; flex: none; }
  .address {
    position: absolute;
    right: 30px;
    bottom: 40px;
    font-weight: 400;
    font-size: 15px;
    line-height: 18px;
  }
</style>
</head>
<body>
<main class="sheet">
  <section class="card card--back" aria-label="Card back">
    <p class="brand-name"><span>Salt Reef</span><span>Cafe</span></p>
  </section>

  <section class="card card--front" aria-label="Card front">
    <p class="brand-name"><span>Salt Reef</span><span>Cafe</span></p>
    <p class="services">Breakfast, Lunch, Dinner, Coffee, Takeaway</p>
    <p class="menu-label">Menu &amp; Opening Hours:</p>
    <ul class="contact-list">
      <li>
        <svg viewBox="0 0 16 16" aria-hidden="true">
          <circle cx="8" cy="8" r="7" fill="none" stroke="currentColor" stroke-width="1.4"/>
          <ellipse cx="8" cy="8" rx="3" ry="7" fill="none" stroke="currentColor" stroke-width="1.2"/>
          <line x1="1" y1="8" x2="15" y2="8" stroke="currentColor" stroke-width="1.2"/>
        </svg>
        www.saltreefcafe.com.au
      </li>
      <li>
        <svg viewBox="0 0 16 16" aria-hidden="true">
          <path d="M3.5 1.5 L6 4 L4.6 5.8 C5.4 7.6 7.6 9.9 10.2 11.4 L12 10 L14.5 12.5 L12.6 14.4 C8 14 2.2 8.4 1.6 3.4 Z" fill="currentColor"/>
        </svg>
        (08) 8461 9273
      </li>
    </ul>
    <p class="address">117 Parade Kelpwater QV 4820</p>
  </section>
</main>
</body>
</html>
```